I need two seperate flyers made
I have supplied 2 x photos of bathrooms, one for each flyer.
First flyer i want a banner or some sort of blockout acccross the bottom with my business name Harwick Bathrooms and my number 0438972605 and the promo is '' Renovate your bathroom from $10990 and in small writing under neath say owner to supply fixtures and tiles

Second flyer to have the same banner accross bottom and the promo is
Complete bathroom renovations from $15990 with small writing under saying terms and conditions apply

Want these to look professional and eye cathcing to generate more work.

I have attached 2x of our old flyers for reference and our current logo for use
Looking forward to working with you.

```html
<!DOCTYPE html>
<html lang="en">
<head>
<meta charset="utf-8">
<title>Harwick Bathrooms – Flyers</title>
<link href="https://fonts.googleapis.com/css2?family=Poppins:wght@400;500;600;700;800&display=swap" rel="stylesheet">
<style>
  :root {
    --stage: #c4c4c4;
    --paper: #ffffff;
    --brand-blue: #1670bd;
    --ink-black: #050505;
    --text-white: #ffffff;
    --photo-warm-light: #cfcbc0;
    --photo-warm-mid: #a9a497;
    --photo-warm-dark: #6e6a60;
    --photo-cool-light: #d9dcdb;
    --photo-cool-mid: #aeb4b2;
    --photo-cool-dark: #7b8280;
  }
  * { box-sizing: border-box; margin: 0; padding: 0; }
  html, body { width: 1200px; height: 1120px; overflow: hidden; }
  body {
    background: var(--stage);
    font-family: "Poppins", sans-serif;
    position: relative;
  }
  .flyer {
    position: absolute;
    top: 203px;
    width: 520px;
    height: 714px;
    background: var(--paper);
    overflow: hidden;
    box-shadow: 0 18px 30px rgba(0,0,0,0.35);
  }
  .flyer--renovate { left: 50px; }
  .flyer--complete { left: 630px; }

  .flyer__photo {
    position: absolute;
    left: 0; top: 0;
    width: 520px; height: 629px;
  }
  .flyer--renovate .flyer__photo {
    background: linear-gradient(160deg, var(--photo-warm-light) 0%, var(--photo-warm-mid) 55%, var(--photo-warm-dark) 100%);
  }
  .flyer--complete .flyer__photo {
    background: linear-gradient(160deg, var(--photo-cool-light) 0%, var(--photo-cool-mid) 55%, var(--photo-cool-dark) 100%);
  }
  .flyer__shade {
    position: absolute;
    left: 0; top: 0;
    width: 520px; height: 629px;
    background:
      linear-gradient(to top, rgba(0,0,0,0.95) 0%, rgba(0,0,0,0.7) 25%, rgba(0,0,0,0) 60%),
      linear-gradient(to right, rgba(0,0,0,0.55) 0%, rgba(0,0,0,0) 60%);
  }
  .flyer__graphics {
    position: absolute;
    left: 0; top: 0;
  }

  .brand-mark {
    position: absolute;
    left: 50px; top: 62px;
    display: flex;
    align-items: center;
    gap: 10px;
    color: var(--text-white);
    font-weight: 400;
  }
  .brand-mark__square {
    width: 14px; height: 14px;
    background: var(--text-white);
  }
  .brand-mark__name {
    font-size: 19px;
    line-height: 1.05;
    letter-spacing: 1px;
  }
  .brand-mark__name span {
    display: block;
    font-size: 10px;
    letter-spacing: 5px;
  }

  .promo {
    position: absolute;
    left: 50px; top: 362px;
    color: var(--text-white);
  }
  .promo__headline {
    font-size: 27px;
    font-weight: 700;
    line-height: 1.22;
    text-transform: uppercase;
  }
  .promo__label {
    margin-top: 12px;
    font-size: 8.5px;
    font-weight: 600;
    color: var(--brand-blue);
    text-transform: uppercase;
  }
  .promo__price {
    font-size: 52px;
    font-weight: 800;
    line-height: 1.08;
    letter-spacing: -0.5px;
  }
  .promo__note {
    margin-top: 2px;
    font-size: 9.5px;
    font-weight: 400;
  }

  .banner__name {
    position: absolute;
    left: 66px; top: 611px;
    color: var(--text-white);
    font-size: 31px;
    font-weight: 800;
    line-height: 0.9;
    text-transform: uppercase;
  }
  .banner__contact {
    position: absolute;
    right: 69px; top: 631px;
    text-align: right;
  }
  .banner__label {
    display: flex;
    align-items: center;
    justify-content: flex-end;
    gap: 3px;
    color: var(--brand-blue);
    font-size: 7.5px;
    font-weight: 700;
    line-height: 1.2;
    text-transform: uppercase;
  }
  .banner__phone {
    margin-top: 2px;
    color: var(--ink-black);
    font-size: 21px;
    font-weight: 500;
    line-height: 1;
    letter-spacing: 0.2px;
  }
</style>
</head>
<body>

<section class="flyer flyer--renovate">
  <div class="flyer__photo" role="img" aria-label="Photo of a renovated bathroom with terrazzo floor, glass shower screen, brass shower fittings, floating white vanity and oval mirror"></div>
  <div class="flyer__shade"></div>
  <svg class="flyer__graphics" width="520" height="714" viewBox="0 0 520 714">
    <polygon points="0,570 190,570 240,629 0,629" fill="#050505"/>
    <line x1="0" y1="515" x2="42" y2="560" stroke="#1670bd" stroke-width="2"/>
    <polygon points="50,602 262,602 301,675 50,675" fill="#1670bd"/>
    <polygon points="275,617 470,617 470,675 306,675" fill="#ffffff" stroke="#1670bd" stroke-width="3"/>
  </svg>
  <div class="brand-mark">
    <div class="brand-mark__square"></div>
    <div class="brand-mark__name">HARWICK<span>BATHROOMS</span></div>
  </div>
  <div class="promo">
    <h1 class="promo__headline">Renovate<br>your bathroom</h1>
    <p class="promo__label">Price starts from</p>
    <p class="promo__price">$10 990</p>
    <p class="promo__note">Owner to supply fixtures and tiles</p>
  </div>
  <p class="banner__name">Harwick<br>Bathrooms</p>
  <div class="banner__contact">
    <p class="banner__label">
      <svg width="8" height="8" viewBox="0 0 10 10"><circle cx="5" cy="5" r="5" fill="#1670bd"/><path d="M3.2 2.6 L4.2 2.6 L4.6 3.8 L4 4.3 Q4.6 5.5 5.7 6 L6.2 5.4 L7.4 5.8 L7.4 6.8 Q5.6 7.4 4.1 5.9 Q2.6 4.4 3.2 2.6Z" fill="#fff"/></svg>
      Call us at
    </p>
    <p class="banner__phone">0438972605</p>
  </div>
</section>

<section class="flyer flyer--complete">
  <div class="flyer__photo" role="img" aria-label="Photo of a renovated bathroom with white herringbone tiles, round backlit mirror, white shaker vanity, freestanding bath and chandelier"></div>
  <div class="flyer__shade"></div>
  <svg class="flyer__graphics" width="520" height="714" viewBox="0 0 520 714">
    <polygon points="0,570 190,570 240,629 0,629" fill="#050505"/>
    <line x1="0" y1="515" x2="42" y2="560" stroke="#1670bd" stroke-width="2"/>
    <polygon points="50,602 262,602 301,675 50,675" fill="#1670bd"/>
    <polygon points="275,617 470,617 470,675 306,675" fill="#ffffff" stroke="#1670bd" stroke-width="3"/>
  </svg>
  <div class="brand-mark">
    <div class="brand-mark__square"></div>
    <div class="brand-mark__name">HARWICK<span>BATHROOMS</span></div>
  </div>
  <div class="promo">
    <h1 class="promo__headline">Complete bathroom<br>renovations</h1>
    <p class="promo__label">Price starts from</p>
    <p class="promo__price">$15 990</p>
    <p class="promo__note">Terms and conditions apply</p>
  </div>
  <p class="banner__name">Harwick<br>Bathrooms</p>
  <div class="banner__contact">
    <p class="banner__label">
      <svg width="8" height="8" viewBox="0 0 10 10"><circle cx="5" cy="5" r="5" fill="#1670bd"/><path d="M3.2 2.6 L4.2 2.6 L4.6 3.8 L4 4.3 Q4.6 5.5 5.7 6 L6.2 5.4 L7.4 5.8 L7.4 6.8 Q5.6 7.4 4.1 5.9 Q2.6 4.4 3.2 2.6Z" fill="#fff"/></svg>
      Call us at
    </p>
    <p class="banner__phone">0438972605</p>
  </div>
</section>

</body>
</html>
```